Can you make FairlyNeat look better than average? We need business cards and a logo refresh :-)

REVISED BRIEF

PRIORITY

VECTOR LOGO

Create a vector version of our existing logo. The logo must not change from its current design, weight or font.

Deliverables

- Logo in blue (#2540BB)
- Logo in white (#FFFFFF)
- Logo in grey (#36454F)
- All logos on transparent background
- All logos in PNG & SVG formats. (SVG must NOT distort stroke width when resized)

BRAND MARK

Create a brand mark for use with the logo. This should be possible to used with the logo and on its own as a stand alone graphical device that represents the FAIRLYNEAT brand.

https://quellbrik.com/resources/glossary/what-is-a-brand-mark

Deliverables

- Brand Mark in blue (#2540BB)
- Brand Mark in white (#FFFFFF)
- Brand Mark in grey (#36454F)
- Brand Mark on transparent background
- Brand Mark in PNG & SVG formats. (SVG must NOT distort stroke width when resized)
- Logo combined with Brand Mark (colours and formats)
.

Business Card Layout

Create 2 layouts with the following details:-

Marcus Delaney
Co-Founder & Chief Product Officer

marcus@fairlyneat.nz
www.fairlyneat.nz
0279831465

Callum Ferris
Founder & CEO

hello@fairlyneat.nz
www.fairlyneat.nz
021 684 2590

DESIGN CONSIDERATIONS

Create versions with ‘Shaping Causes With Heart’ tag line incorporated within the design and without (maintain separation of logo from tag line)

- Create a version with and without the brand mark
- Keep it clean and simple but elevate the design with subtle design effects
- Consider use of raised spot gloss colour (this can be white on white for subtle or blue on blue or blue on white)
- Consider use of spot gloss colour (this can be white on white for subtle or blue on blue or blue on white)
- Consider use of letterpress indentation
- Ensure contact details are legible, use sans-serif font

PREVIOUS BRIEF

We need a business card design for our business FairlyNeat. We are a purpose driven brand and media agency that helps brands and charities plan and buy traditional media campaigns (TV, Radio, Print, Outdoor etc). We give a significant amount of the media booking fees we receive from media vendors to charity in the name of our clients. https://www.plinkwork.com/posts/wearefairlyneat_giveback-fairlyneat-shapingcauseswithheart-activity-5829170364418205731-Rtqe

Our strapline is 'Shaping Causes With Heart'.

We want to keep our logo design as it is but it does need tightening up and made into a proper vector image as it's been created from a font.

Our brand colour is #2540BB and we need to keep this.

Our brand is professional but human, warm and engaging and doesn't take itself too seriously.

Things We Need
- vectorisation and tidying up of existing logo
- We'd like you to think about how we can incorporate a brand mark with the logo to add another dimension to our brand
- business card layout and design
- we'll be using zentiprint.com to print the cards so please take a look at the options they have (spot gloss, foil, letterpress, square cards and even the backs of the cards can have a different design on every single card!
- potential opportunity for different famous quotes on the back or imagery or slight design differences
- we'd be open to the use of an emoji or emojiis as the brandmark or to be incorporated into the card designs
- we can have as many different design batches as we like for the backs of the cards

https://www.zentiprint.com/au/business-cards

We want to make an impact, we want to be seen as professional but fun, we want to be different.

Here's a press release of what we're about.

https://adwirely.co.nz/movings-shakings/fairlyneat-welcomes-marcus-delaney-as-co-founder/

Be bold, be different, there is no such thing as a bad idea. We're open to anything so please bring your best ideas and have fun with it! Go crazy if you like!
____________
Marcus Delaney
marcus@fairlyneat.nz
0279831465

Callum Ferris
Founder & CEO
hello@fairlyneat.nz
021 684 2590

Shaping Causes With Heart

________

These are the only details we MUST have on the cards, the rest is up to you. Just make sure you use all of your creativity but don't feel the need to crowd the card with too much, let it breathe as well.

In terms of font for the details, we'll leave that up to you, just ensure it's legible. Oh and please don't take any design inspiration from our website - that will be changing!

Please don't let the design and layout look cheap and tacky though. It needs to still feel premium but personable.

Thanks

Marcus

Many designs are changing the logo and this was NOT in the brief. We need a brand mark to complement the logo. We need to see the logo with and without the brand mark. We need to see the business card with both logo + brand mark and logo on its own We need to see the business card with and without the tagline 'Shaping Causes With Heart'

purpose driven Brand & Media Agency

Shaping Causes With Heart
Marcus Delaney, Co-Founder & Chief Product Officer, marcus@fairlyneat.nz fairlyneet.nz, 0279 831 465

Callum Ferris, Founder & CEO hello@fairlyneat.nz, fairlyneet.nz, 021 684 2590

Serif
Sans Serif

0054AA
0677BA
7BADD7
CADEEF
E8F1F8

• brand mark, vector version of existing logo, Shaping Causes With Heart tagline, existing logo traced and vectorised. Must fully explore the design options from zentiprint.com that can enhance the overall card design
• brandmark to help elevate the logo, maybe incorporate some other design elements into the card like lines, or grids.
• A cheap look and feel

```html
<!DOCTYPE html>
<html lang="en">
<head>
<meta charset="utf-8">
<title>FairlyNeat — Business Card</title>
<link href="https://fonts.googleapis.com/css2?family=Montserrat:wght@500;600;700&display=swap" rel="stylesheet">
<style>
  :root {
    --brand-blue: #2540BB;
    --blue-tint: #3456E2;
    --paper: #FFFFFF;
    --backdrop: #2B2B2B;
    --card-shadow: rgba(0,0,0,0.45);
  }
  * { box-sizing: border-box; margin: 0; padding: 0; }
  html, body { width: 1200px; height: 900px; overflow: hidden; }
  body { background: var(--backdrop); font-family: 'Montserrat', sans-serif; }

  .card {
    position: absolute;
    top: 292px;
    width: 530px;
    height: 315px;
    border-radius: 26px;
    overflow: hidden;
    box-shadow: 0 6px 14px var(--card-shadow);
  }
  .card--back { left: 70px; background: var(--brand-blue); }
  .card--front { left: 615px; background: var(--paper); color: var(--brand-blue); }

  .brand-name {
    font-family: 'Montserrat', sans-serif;
    font-weight: 700;
    white-space: nowrap;
    line-height: 1;
  }
  .card--back .brand-name--small {
    position: absolute; right: 26px; top: 36px;
    font-size: 20px; color: var(--paper);
  }
  .card--back .brand-name--bleed {
    position: absolute; left: -6px; bottom: -10px;
    font-size: 66px; color: var(--blue-tint);
  }

  .person { position: absolute; left: 50px; }
  .person--primary { top: 40px; }
  .person--secondary { top: 246px; }
  .person-name { font-weight: 700; font-size: 17px; letter-spacing: 0.3px; text-transform: uppercase; }
  .person-role { font-weight: 600; font-size: 13.5px; line-height: 17px; margin-top: 2px; }

  .contact {
    position: absolute; left: 266px;
    border-left: 2px solid var(--brand-blue);
    padding-left: 8px;
    display: flex; flex-direction: column; justify-content: flex-start; gap: 2px;
  }
  .contact--primary { top: 34px; height: 66px; padding-top: 14px; }
  .contact--secondary { top: 232px; height: 64px; padding-top: 14px; }
  .contact-line { display: flex; align-items: center; gap: 7px; font-weight: 500; font-size: 13.5px; }
  .contact-line svg { width: 11px; height: 11px; fill: var(--brand-blue); flex: none; }

  .front-name {
    position: absolute; left: 50px; top: 133px;
    font-size: 52px; color: var(--brand-blue);
  }
  .tagline {
    position: absolute; left: 50px; right: 40px; top: 192px;
    text-align: center; font-weight: 500; font-size: 13px;
    letter-spacing: 4.6px; text-transform: uppercase;
  }
</style>
</head>
<body>

<section class="card card--back" aria-label="Card back">
  <div class="brand-name brand-name--small">FAIRLYNEAT.</div>
  <div class="brand-name brand-name--bleed" aria-hidden="true">FAIRLYNEAT.</div>
</section>

<section class="card card--front" aria-label="Card front">
  <div class="person person--primary">
    <div class="person-name">Marcus Delaney</div>
    <div class="person-role">Co-Founder &amp;<br>Chief Product Officer</div>
  </div>
  <div class="contact contact--primary">
    <div class="contact-line">
      <svg viewBox="0 0 12 12" aria-hidden="true"><path d="M0 2h12v1.2L6 7 0 3.2z M0 4.6l6 3.8 6-3.8V10H0z"/></svg>
      marcus@fairlyneat.nz
    </div>
    <div class="contact-line">
      <svg viewBox="0 0 12 12" aria-hidden="true"><path d="M1 4.5C1 2.5 3.5 1.5 6 1.5s5 1 5 3l-2 .8-1-1.3H4L3 5.3z M3.5 6h5l1.5 4.5H2z"/></svg>
      0279 831 465
    </div>
  </div>

  <div class="brand-name front-name">FAIRLYNEAT.</div>
  <div class="tagline">Shaping Causes With Heart</div>

  <div class="person person--secondary">
    <div class="person-name">Callum Ferris</div>
    <div class="person-role">Founder &amp; CEO</div>
  </div>
  <div class="contact contact--secondary">
    <div class="contact-line">
      <svg viewBox="0 0 12 12" aria-hidden="true"><path d="M0 2h12v1.2L6 7 0 3.2z M0 4.6l6 3.8 6-3.8V10H0z"/></svg>
      hello@fairlyneat.nz
    </div>
    <div class="contact-line">
      <svg viewBox="0 0 12 12" aria-hidden="true"><path d="M1 4.5C1 2.5 3.5 1.5 6 1.5s5 1 5 3l-2 .8-1-1.3H4L3 5.3z M3.5 6h5l1.5 4.5H2z"/></svg>
      021 684 2590
    </div>
  </div>
</section>

</body>
</html>
```